My portfolio needs a makeover! Clean, modern portfolio website needed for tech professional

I need a modern, updated design for my existing portfolio site (https://marelovic.folioshelf.example/). I am a content professional who has done a lot of different types of content work for big companies. I don't really have a title.

I want to stay simple and clean, but also can be a little whimsical, fun, and a little colorful to go along with the logo I just selected.

I have a domain on Pageloom (marelovic.com), but I’d be willing to move my domain to another site for the right design.

I would like it coded/configured and deployed, but I need the ability to update the site myself later to easily switch out my portfolio pieces. I’m not very good at html/xml.

Pages needed:
Home page
Who I am
How to reach me
What I do > By Craft (in the nav, this will be a dropdown under What I Do)
What I do > By Brand (in the nav, this will be a dropdown under What I Do)

Please see Website Design Doc for details!

Requirements
Must have
• Design must include these pages:
1. Homepage
2. Who I Am
3. What I Do
- By Brand
- By Craft
4. How to Reach Me
Nice to have
• Example portfolio sites I like:
https://www.drivenquarry.example/
http://jolesumner.example/
https://www.tdvarnock.example/
https://www.oriannebelcastro.example/

For my portfolio pieces, I like either tiles or a carousel.

```html
<!DOCTYPE html>
<html lang="en">
<head>
<meta charset="utf-8">
<title>Mara Lovic — Content</title>
<link href="https://fonts.googleapis.com/css2?family=Montserrat:wght@400;500;600;800&display=swap" rel="stylesheet">
<style>
  :root {
    --sky: #2aa9e2;
    --white: #ffffff;
    --ink-dark: #1c2128;
    --photo-a: #6b6a66;
    --photo-b: #3a3b3e;
    --photo-c: #24262a;
    --ring-blue: #2f7fb0;
    --ring-olive: #8a9231;
    --ring-purple: #8d6ba8;
    --ring-red: #b3333a;
    --ring-yellow: #c9b52a;
  }
  * { box-sizing: border-box; margin: 0; padding: 0; }
  html, body { width: 1200px; height: 857px; overflow: hidden; }
  body { font-family: "Montserrat", sans-serif; color: var(--white); background: var(--photo-c); }
  .hero { position: relative; width: 1200px; height: 857px; overflow: hidden; }
  .hero-photo {
    position: absolute; inset: 0;
    background:
      radial-gradient(ellipse 320px 260px at 600px 360px, #8a8b8f 0%, rgba(138,139,143,0) 100%),
      radial-gradient(ellipse 500px 400px at 600px 150px, #7c7a74 0%, rgba(124,122,116,0) 100%),
      linear-gradient(180deg, var(--photo-a) 0%, var(--photo-b) 55%, var(--photo-c) 100%);
  }
  .hero-shade { position: absolute; inset: 0; background: rgba(20,24,30,0.42); }
  .rings { position: absolute; inset: 0; }
  .site-header { position: absolute; left: 0; top: 0; width: 100%; height: 120px; }
  .brand { position: absolute; left: 112px; top: 68px; display: flex; align-items: center; gap: 10px; }
  .brand-dot { width: 14px; height: 14px; border-radius: 50%; background: var(--sky); }
  .brand-name { font-weight: 800; font-size: 28px; letter-spacing: 0.5px; color: var(--sky); }
  .main-nav { position: absolute; left: 388px; top: 52px; display: flex; gap: 46px; font-size: 15.5px; font-weight: 500; }
  .main-nav a { color: var(--white); text-decoration: none; }
  .caret { display: inline-block; margin-left: 4px; vertical-align: middle; }
  .social-btn {
    position: absolute; left: 920px; top: 40px; width: 168px; height: 43px;
    border-radius: 22px; background: var(--sky); color: var(--white);
    font-weight: 600; font-size: 16px; display: flex; align-items: center; justify-content: center; text-decoration: none;
  }
  .headline {
    position: absolute; left: 0; top: 312px; width: 100%;
    text-align: center; font-weight: 800; font-size: 50px; line-height: 56px; text-transform: uppercase; letter-spacing: -0.5px;
  }
  .cta {
    position: absolute; left: 516px; top: 493px; width: 168px; height: 43px;
    border-radius: 22px; background: var(--sky); color: var(--white);
    font-weight: 600; font-size: 15.5px; display: flex; align-items: center; justify-content: center; text-decoration: none;
  }
  .site-footer { position: absolute; left: 0; top: 830px; width: 100%; text-align: center; font-size: 11.5px; font-weight: 500; }
</style>
</head>
<body>
<main class="hero">
  <div class="hero-photo" role="img" aria-label="Overhead photo of people working together, one typing on a laptop and one writing in a notebook"></div>
  <div class="hero-shade"></div>

  <svg class="rings" width="1200" height="857" viewBox="0 0 1200 857" aria-hidden="true" fill="none">
    <circle cx="450" cy="75" r="56" stroke="var(--ring-blue)" stroke-width="10" opacity="0.55"/>
    <circle cx="146" cy="324" r="120" stroke="var(--ring-olive)" stroke-width="2.5" opacity="0.75"/>
    <circle cx="936" cy="266" r="62" stroke="var(--ring-purple)" stroke-width="3" opacity="0.7"/>
    <circle cx="1056" cy="713" r="94" stroke="var(--ring-red)" stroke-width="4" opacity="0.8"/>
    <circle cx="111" cy="763" r="73" stroke="var(--ring-yellow)" stroke-width="9" opacity="0.7"/>
    <circle cx="476" cy="857" r="56" stroke="var(--ring-blue)" stroke-width="8" opacity="0.55"/>
  </svg>

  <header class="site-header">
    <div class="brand"><span class="brand-dot"></span><span class="brand-name">MARA LOVIC</span></div>
    <nav class="main-nav">
      <a href="#">Home</a>
      <a href="#">Who I Am</a>
      <a href="#">What I Do<svg class="caret" width="9" height="6" viewBox="0 0 9 6"><path d="M1 1l3.5 3.5L8 1" stroke="#fff" stroke-width="1.6" fill="none"/></svg></a>
      <a href="#">How to Reach Me</a>
    </nav>
    <a class="social-btn" href="#">ProLink</a>
  </header>

  <h1 class="headline">Versatile resource experienced<br>in all phases of digital product<br>development</h1>
  <a class="cta" href="#">Get Started</a>

  <footer class="site-footer">Copyrights © The Company name 2020 | Allrights Reserved</footer>
</main>
</body>
</html>
```